Child Care Centre needs new roadside billboard / sign*

We have a 2400mm x 1200mm sign that needs to be refreshed. The design is dated and we want to create a new cleaner, more readable roadside signIt needs to be readable from about 100m awayThe text requirements are simple, but we need it to have a warm, family feel.We are located in a small beach side community and we have a lot of bright colours in our centre (a lot of blues and yellows)https://www.saltmarshchildcare.com.au/

Target Market(s)

Parents of young children

Industry/Entity Type

Childcare

Colors
fbed22
0355a3

Requirements
Must have
• Readable from c.100m
• Simple, warm design
Should not have
• Cluttered or overly busy

```html
<!DOCTYPE html>
<html lang="en">
<head>
<meta charset="utf-8">
<title>Saltmarsh Early Education – Roadside Sign</title>
<link rel="stylesheet" href="https://fonts.googleapis.com/css2?family=Bubblegum+Sans&family=Delius&display=swap">
<style>
  :root {
    --ocean-blue: #0355a3;
    --sun-yellow: #fbed22;
    --sun-deep: #f7b912;
    --sun-warm: #fcd21e;
    --signal-red: #e3202b;
    --ink: #111111;
    --paper: #ffffff;
  }
  * { margin: 0; padding: 0; box-sizing: border-box; }
  html, body {
    width: 1200px; height: 900px; overflow: hidden;
    background: var(--paper);
  }
  .canvas { position: relative; width: 1200px; height: 900px; }
  .sign {
    position: absolute; left: 52px; top: 185px;
    width: 1099px; height: 543px;
    overflow: hidden;
    background: var(--ocean-blue);
    box-shadow: 2px 3px 4px rgba(0,0,0,0.25);
  }
  .sign-backdrop { position: absolute; inset: 0; width: 100%; height: 100%; }
  .mascot-area {
    position: absolute; left: 128px; top: 58px;
    width: 207px; height: 405px;
    border-radius: 90px 90px 70px 70px;
    background: radial-gradient(ellipse at 50% 45%, #fff46a 0%, var(--sun-yellow) 55%, #f2d70f 100%);
  }
  .line {
    position: absolute; left: 645px;
    transform: translate(-50%, -50%);
    white-space: nowrap; line-height: 1;
    font-family: "Bubblegum Sans", "Comic Sans MS", cursive;
    text-transform: uppercase;
  }
  .brand-name { top: 63px; font-size: 78px; color: var(--ocean-blue); text-transform: none; }
  .brand-tagline { top: 127px; font-size: 46px; color: var(--ink); font-family: "Delius", "Comic Sans MS", cursive; text-transform: none; }
  .primary { color: var(--ocean-blue); font-size: 44px; }
  .secondary { color: var(--signal-red); font-size: 31px; }
  .ages { top: 185px; }
  .long-day { top: 222px; }
  .hours { top: 259px; word-spacing: 4px; }
  .hours .gap { display: inline-block; width: 26px; }
  .year-round { top: 299px; }
  .school-care { top: 336px; }
  .vacation { top: 376px; }
  .phone {
    top: 460px; left: 614px;
    font-size: 96px; color: var(--signal-red);
    letter-spacing: 1px;
    text-shadow:
      3px 0 0 var(--paper), -3px 0 0 var(--paper),
      0 3px 0 var(--paper), 0 -3px 0 var(--paper),
      2px 2px 0 var(--paper), -2px -2px 0 var(--paper),
      2px -2px 0 var(--paper), -2px 2px 0 var(--paper);
  }
</style>
</head>
<body>
<main class="canvas">
  <section class="sign" aria-label="Saltmarsh Early Education roadside sign">
    <svg class="sign-backdrop" viewBox="0 0 1221 603" preserveAspectRatio="none" aria-hidden="true">
      <defs>
        <radialGradient id="sun-glow" cx="0.45" cy="0.45" r="0.75">
          <stop offset="0" stop-color="#fde23a"/>
          <stop offset="0.6" stop-color="#fcd21e"/>
          <stop offset="1" stop-color="#f7b912"/>
        </radialGradient>
      </defs>
      <path d="M92,0 C30,160 150,340 420,480 C640,570 920,530 1221,450 L1221,0 Z" fill="#ffffff"/>
      <path d="M148,0 C95,150 205,315 440,445 C650,535 920,495 1221,420 L1221,0 Z" fill="url(#sun-glow)"/>
    </svg>

    <div class="mascot-area" role="img" aria-label="Cartoon seahorse mascot wearing a graduation cap and holding a diploma"></div>

    <h1 class="line brand-name">Saltmarsh</h1>
    <p class="line brand-tagline">Early Education</p>

    <p class="line primary ages">6 weeks to 6 years</p>
    <p class="line secondary long-day">Long day care</p>
    <p class="line primary hours">Open 6:30 am<span class="gap"></span>6:30 pm</p>
    <p class="line secondary year-round">52 weeks a year</p>
    <p class="line primary school-care">Before and after school care</p>
    <p class="line secondary vacation">Vacation care</p>

    <p class="line phone">07·4100·2836</p>
  </section>
</main>
</body>
</html>
```